Bluestone Advisory & Mgmt - Professional Business Cards

Hi!

I am a Real Estate Developer and Construction Consultant.

I have a lot of inspiration from previous designs and would be open to using the attached Designs as a starting point. I would like to see these styles incorporated into your designs.

I really need professional business card to go with it that includes my important info.

Look forward to seeing your designs!.

Target Market(s)

My Target market are building owners, lawyers, consultants.

Industry/Entity Type

Real Estate Development

Contact Information for Business Card

My Name: Dorian Pelkey
My Title: Principle
Company Name: Bluestone Advisory & Mgmt, LLC
Address: 348 West 71st Street, 9th FL New York, NY 10010
Mobile: 917.806.3971
Website: bam-hvx.example

Font styles to use
Serif
Sans Serif

Colors

Designer to choose colors to be used in the design.

Requirements
Must have
• Must incorporate the logo attached or have new that looks similar.
• Must use professional font that will be seen and judged by wealthy land owners and developers.
• Must incorporate some of the color green.
Should not have
• Photo's or pictures of people or buildings of any kind.

```html
<!DOCTYPE html>
<html lang="en">
<head>
<meta charset="utf-8">
<title>Bluestone Advisory &amp; Mgmt - Business Cards</title>
<link href="https://fonts.googleapis.com/css2?family=Montserrat:wght@400;500;700;800&display=swap" rel="stylesheet">
<style>
  :root {
    --backdrop: #2a2e33;
    --card: #151515;
    --green: #3fb871;
    --grey: #a7a2a2;
    --text: #d9d9d9;
    --white: #ffffff;
  }
  * { box-sizing: border-box; margin: 0; padding: 0; }
  html, body { width: 1200px; height: 900px; overflow: hidden; }
  body {
    background: var(--backdrop);
    font-family: "Montserrat", Arial, sans-serif;
    display: flex; align-items: center; justify-content: center; gap: 50px;
  }
  .card {
    width: 540px; height: 309px; background: var(--card);
    position: relative; box-shadow: 0 18px 40px rgba(0,0,0,.45);
  }
  /* Front: contact details */
  .brand-row { position: absolute; left: 34px; top: 30px; display: flex; align-items: center; }
  .brand-mark { font-weight: 800; font-size: 44px; color: var(--green); letter-spacing: -1px; line-height: 1; }
  .brand-divider { width: 1.5px; height: 48px; background: var(--grey); margin: 0 12px; }
  .brand-name { font-size: 30px; color: var(--green); line-height: 1; }
  .brand-sub { font-size: 17px; color: var(--grey); margin-top: 3px; }
  .person { position: absolute; left: 34px; top: 100px; }
  .person-name { font-size: 17px; font-weight: 500; color: var(--green); text-transform: uppercase; letter-spacing: .5px; }
  .person-title { font-size: 12px; color: var(--green); margin-top: 2px; }
  .contact-list { position: absolute; left: 34px; top: 150px; list-style: none; }
  .contact-list li { display: flex; align-items: center; gap: 9px; font-size: 12.5px; color: var(--text); line-height: 19px; }
  .contact-list svg { width: 12px; height: 12px; flex: none; }
  .card-rule { position: absolute; left: 34px; right: 34px; top: 214px; height: 1px; background: var(--green); }
  .address { position: absolute; left: 34px; top: 226px; font-size: 12.5px; color: var(--text); line-height: 19px; }
  /* Back: logo side */
  .back-mark {
    position: absolute; left: 0; right: 0; top: 78px; text-align: center;
    font-weight: 800; font-size: 92px; color: var(--grey); letter-spacing: -2px; line-height: 1;
  }
  .back-url {
    position: absolute; left: 150px; right: 150px; top: 218px; text-align: center;
    font-weight: 700; font-size: 13px; color: var(--white); padding-bottom: 8px;
    border-bottom: 2px solid var(--white);
  }
</style>
</head>
<body>
  <section class="card card-front">
    <div class="brand-row">
      <span class="brand-mark">BAM</span>
      <span class="brand-divider"></span>
      <div>
        <div class="brand-name">Bluestone</div>
        <div class="brand-sub">Advisory Management</div>
      </div>
    </div>
    <div class="person">
      <div class="person-name">Dorian Pelkey</div>
      <div class="person-title">Principle</div>
    </div>
    <ul class="contact-list">
      <li><svg viewBox="0 0 12 12"><circle cx="6" cy="6" r="5.3" fill="none" stroke="#3fb871"/><path d="M4 3.3l1 1.4-.6.7a4 4 0 0 0 2.2 2.2l.7-.6 1.4 1-.6 1C6 9 3 6 3.2 3.9z" fill="#3fb871"/></svg>917.806.3971</li>
      <li><svg viewBox="0 0 12 12"><rect x="1" y="2.5" width="10" height="7" fill="none" stroke="#3fb871"/><path d="M1 2.5l5 4 5-4" fill="none" stroke="#3fb871"/></svg>dorian@bam-hvx.example</li>
      <li><svg viewBox="0 0 12 12"><circle cx="6" cy="6" r="5.3" fill="#3fb871"/><path d="M.7 6h10.6M6 .7c-2.5 3-2.5 7.6 0 10.6M6 .7c2.5 3 2.5 7.6 0 10.6" fill="none" stroke="#151515" stroke-width=".8"/></svg>www.bam-hvx.example</li>
    </ul>
    <div class="card-rule"></div>
    <address class="address" style="font-style:normal">348 West 71st Street<br>9th FL New York, NY 10010</address>
  </section>

  <section class="card card-back">
    <div class="back-mark">BAM</div>
    <div class="back-url">www.bam-hvx.example</div>
  </section>
</body>
</html>
```